Modify mobile web Photoshop design to make them look great

We need to choose and refine the stock image to look great on 5 mobile web pages: 1) Hourglass image on home screen, 2) Sofa image on registration screen, 3) Loveseat image on login screen, 4) Lamp for reminder screen, and 5) Bed for ratings / score screen. Sample photos denote what customer wants, but they are just downloaded from Vantry, and is not purchased stock photos. Designers need to show that the updated photos used are properly purchased from stock photo source. Photoshop files for all 5 mobile web pages are provided. Artists are requested to edit and submit the 5 photoshop files and make them look as good as possible with the constraints above. No change is needed on the layout or anything beside the 5 stock images, but subtle refinements are OK if you believe it would improve the overall design without affecting the art direction.

Target Market(s)

Travel, Lifestyle

Industry/Entity Type

Hospitality

Font styles to use
Sans Serif

Requirements
Must have
• Stock photos must be properly licensed, artists must put updated stock photos back into supplied photoshop source files, updated look and feel should have the same general art direction, images must be hourglass, sofa, loveseat, lamp and bed
Nice to have
• Minor and very subtle touchup of other elements without affecting any design work of the layout such as color scheme
Should not have
• Should not affect art direction, identity and color of all design and layout elements, should not use stock image other than the types specified (hourglass, sofa, loveseat, lamp and bed), should not use images not licensed from stock photo sites

```html
<!DOCTYPE html>
<html lang="en">
<head>
<meta charset="utf-8">
<title>lodgera – Register</title>
<link rel="stylesheet" href="https://fonts.googleapis.com/css2?family=Lato:wght@400;700&family=Montserrat:wght@700;800&display=swap">
<style>
  :root {
    --white: #ffffff;
    --ink: #111111;
    --text-muted: #555555;
    --wall-top: #f6e8d6;
    --wall-mid: #f1dcc2;
    --baseboard: #f4ece4;
    --floor: #c68650;
    --floor-dark: #9c5e33;
    --sofa-light: #d6d2d3;
    --sofa-mid: #c4bfc1;
    --sofa-shade: #a9a4a6;
    --card-fill: rgba(236, 226, 214, 0.82);
    --card-edge: rgba(255, 255, 255, 0.9);
    --lilac: #b07fdc;
    --teal: #0e9494;
    --magenta: #a3177f;
    --peach: #f3a66c;
    --orange: #f49d5a;
    --rule: #cfcfcf;
  }
  * { box-sizing: border-box; margin: 0; padding: 0; }
  html, body { width: 675px; height: 1200px; overflow: hidden; background: var(--white); }
  body { position: relative; font-family: "Lato", Arial, sans-serif; }

  .status-bar {
    position: absolute; top: 0; left: 0; width: 675px; height: 38px;
    display: flex; align-items: center; justify-content: space-between;
    padding: 0 14px 0 24px; font-size: 18px; color: var(--ink); background: var(--white);
  }
  .status-bar .carrier { display: flex; align-items: center; gap: 8px; }
  .status-bar .time { position: absolute; left: 0; right: 0; text-align: center; font-weight: 700; pointer-events: none; }

  .app-header {
    position: absolute; top: 38px; left: 0; width: 675px; height: 87px;
    background: var(--white);
  }
  .app-header .back { position: absolute; left: 33px; top: 25px; }
  .app-header .menu { position: absolute; left: 603px; top: 27px; }
  .brand-name {
    position: absolute; left: 0; right: 0; top: 12px; text-align: center;
    font-family: "Montserrat", Arial, sans-serif; font-weight: 800; font-size: 44px;
    letter-spacing: -2px; color: var(--ink);
  }

  .room-backdrop {
    position: absolute; top: 125px; left: 0; width: 675px; height: 1075px;
    background: linear-gradient(180deg,
      var(--wall-top) 0%, var(--wall-mid) 70%, #ecd3b4 84%,
      var(--baseboard) 84%, var(--baseboard) 86.6%,
      var(--floor) 86.6%, var(--floor-dark) 100%);
  }

  .sofa-photo {
    position: absolute; left: 146px; top: 832px; width: 414px; height: 262px;
    border-radius: 22px 22px 10px 10px;
    background: linear-gradient(180deg, var(--sofa-light) 0%, var(--sofa-mid) 62%, var(--sofa-shade) 84%, #5a3a28 84%, #5a3a28 100%);
  }

  .register-card {
    position: absolute; left: 72px; top: 198px; width: 530px; height: 563px;
    background: var(--card-fill); border: 1px solid var(--card-edge); border-radius: 8px;
  }

  .field {
    position: absolute; left: 38px; width: 454px; height: 53px;
    background: var(--white); border-radius: 6px; border-bottom: 1px solid var(--lilac);
    display: flex; align-items: center;
  }
  .field .icon { width: 49px; display: flex; justify-content: center; align-items: center; }
  .field .divider { width: 1px; height: 32px; background: var(--rule); }
  .field .label { margin-left: 17px; font-size: 16.5px; color: var(--text-muted); flex: 1; }
  .field .trail { margin-right: 18px; display: flex; }
  .field--name { top: 46px; }
  .field--id { top: 113px; border-bottom-color: #5a6d7a; }
  .field--dob { top: 181px; }
  .field--phone { top: 248px; border-bottom-color: #7f8a93; }
  .field--password { top: 316px; border-bottom-color: var(--teal); }
  .field--email { top: 383px; border-bottom-color: #6f7c87; }
  .dob-tag { font-size: 13px; color: var(--magenta); }

  .register-button {
    position: absolute; left: 38px; top: 464px; width: 454px; height: 54px;
    background: var(--orange); border: 0; border-radius: 3px; color: var(--white);
    font-family: "Montserrat", Arial, sans-serif; font-weight: 700; font-size: 17px; letter-spacing: 0.5px;
  }

  .page-dots { position: absolute; top: 1111px; left: 276px; display: flex; gap: 12px; }
  .page-dots span { width: 18px; height: 18px; border-radius: 50%; display: block; }
</style>
</head>
<body>
  <div class="status-bar">
    <span class="carrier">Carrier
      <svg width="20" height="15" viewBox="0 0 20 15"><path d="M10 14l3-3.4a4.2 4.2 0 0 0-6 0z M3.6 7.2l1.7 1.9a6.7 6.7 0 0 1 9.4 0l1.7-1.9a9.3 9.3 0 0 0-12.8 0z M0.4 3.6l1.7 1.9a11.2 11.2 0 0 1 15.8 0l1.7-1.9a13.8 13.8 0 0 0-19.2 0z" fill="#111"/></svg>
    </span>
    <span class="time">1:23 PM</span>
    <svg width="42" height="18" viewBox="0 0 42 18"><rect x="1" y="1" width="36" height="16" rx="3" fill="none" stroke="#111" stroke-width="1.5"/><rect x="3" y="3" width="32" height="12" rx="1.5" fill="#111"/><rect x="38.5" y="6" width="2.5" height="6" rx="1" fill="#111"/></svg>
  </div>

  <header class="app-header">
    <svg class="back" width="22" height="34" viewBox="0 0 22 34"><path d="M18 3L5 17l13 14" fill="none" stroke="#111" stroke-width="4.5" stroke-linecap="round" stroke-linejoin="round"/></svg>
    <div class="brand-name">lodgera</div>
    <svg class="menu" width="37" height="31" viewBox="0 0 37 31"><g stroke="#111" stroke-width="4.5" stroke-linecap="round"><line x1="3" y1="3" x2="34" y2="3"/><line x1="3" y1="15.5" x2="34" y2="15.5"/><line x1="3" y1="28" x2="34" y2="28"/></g></svg>
  </header>

  <div class="room-backdrop" role="img" aria-label="Licensed stock photo of a warm cream living room wall with a white baseboard and wooden floor"></div>
  <div class="sofa-photo" role="img" aria-label="Licensed stock photo of a grey tufted sofa on wooden legs with a turquoise cushion"></div>

  <form class="register-card">
    <div class="field field--name">
      <span class="icon"><svg width="22" height="24" viewBox="0 0 22 24"><circle cx="11" cy="7" r="5" fill="none" stroke="#b07fdc" stroke-width="1.5"/><path d="M1.5 22.5c0-5 4.3-8 9.5-8s9.5 3 9.5 8z" fill="none" stroke="#b07fdc" stroke-width="1.5"/></svg></span>
      <span class="divider"></span><span class="label">Full Name</span>
    </div>
    <div class="field field--id">
      <span class="icon"><svg width="30" height="20" viewBox="0 0 30 20"><rect x="1" y="1" width="28" height="18" rx="1.5" fill="none" stroke="#0e9494" stroke-width="1.5"/><circle cx="9" cy="8" r="2.6" fill="none" stroke="#0e9494" stroke-width="1.3"/><path d="M4.5 15.5c0-2.6 2-4 4.5-4s4.5 1.4 4.5 4z" fill="none" stroke="#0e9494" stroke-width="1.3"/><g stroke="#0e9494" stroke-width="1.5"><line x1="17" y1="7" x2="25" y2="7"/><line x1="17" y1="10.5" x2="25" y2="10.5"/><line x1="17" y1="14" x2="25" y2="14"/></g></svg></span>
      <span class="divider"></span><span class="label">ID Number</span>
    </div>
    <div class="field field--dob">
      <span class="icon"><span class="dob-tag">DOB</span></span>
      <span class="divider"></span><span class="label">06/09/1980</span>
      <span class="trail"><svg width="24" height="25" viewBox="0 0 24 25"><rect x="1" y="3" width="22" height="21" rx="2" fill="#a3177f"/><rect x="5" y="0.5" width="3" height="5" rx="1" fill="#a3177f"/><rect x="16" y="0.5" width="3" height="5" rx="1" fill="#a3177f"/><rect x="3" y="8" width="18" height="14" fill="#fff"/><g fill="#a3177f"><rect x="5" y="10" width="3" height="3"/><rect x="10.5" y="10" width="3" height="3"/><rect x="16" y="10" width="3" height="3"/><rect x="5" y="16" width="3" height="3"/><rect x="10.5" y="16" width="3" height="3"/><rect x="16" y="16" width="3" height="3"/></g></svg></span>
    </div>
    <div class="field field--phone">
      <span class="icon"><svg width="16" height="28" viewBox="0 0 16 28"><rect x="1" y="1" width="14" height="26" rx="2" fill="none" stroke="#f3a66c" stroke-width="1.5"/><rect x="3" y="5" width="10" height="16" fill="#f3a66c"/><circle cx="8" cy="24" r="1.2" fill="#f3a66c"/></svg></span>
      <span class="divider"></span><span class="label">Mobile Phone Number</span>
    </div>
    <div class="field field--password">
      <span class="icon"><svg width="24" height="24" viewBox="0 0 24 24"><circle cx="16" cy="8" r="6.5" fill="#0e9494"/><circle cx="17.5" cy="6.5" r="1.8" fill="#fff"/><g stroke="#0e9494" stroke-width="3.2" stroke-linecap="round"><line x1="12" y1="12" x2="3" y2="21"/><line x1="5" y1="19" x2="7.5" y2="21.5"/><line x1="7.5" y1="16.5" x2="9.5" y2="18.5"/></g></svg></span>
      <span class="divider"></span><span class="label">Set Password</span>
    </div>
    <div class="field field--email">
      <span class="icon"><svg width="22" height="16" viewBox="0 0 22 16"><rect x="0" y="0" width="22" height="16" fill="#b48fe0"/><path d="M0 0l11 9 11-9M0 16l8-7M22 16l-8-7" fill="none" stroke="#fff" stroke-width="1.2"/></svg></span>
      <span class="divider"></span><span class="label">Email</span>
    </div>
    <button class="register-button" type="button">REGISTER NOW</button>
  </form>

  <nav class="page-dots" aria-label="Pages">
    <span style="background: var(--lilac)"></span>
    <span style="background: var(--teal)"></span>
    <span style="background: var(--magenta)"></span>
    <span style="background: var(--peach)"></span>
    <span style="background: var(--teal)"></span>
  </nav>
</body>
</html>
```